Vortique Energy Business Card Design

website: www.vortiqueenergy.example
Project: Business Card Design for Vortique Energy
Name: Derek Holloway
Title: Founder / Operations Strategist
Visual Identity & Logo:
Logo File: VRT-Logo-FullGradient-Final.png (Attached).
Color Palette: The brand relies on a distinctive Cyan (Blue) to Lime Green gradient.
Background Preference: We want a Dark Mode aesthetic (Deep Matte Black, Charcoal, or Dark Slate) to make the neon gradient of the logo pop. This feels more "tech/industrial" than a standard white card.
Design Aesthetic (The "Ops" Vibe):
Concept: "Grid & Infrastructure." We are a solar rental company, focusing on logistics and access.
Typography: White, bold sans-serif text for contact info. High contrast against the dark background.
Accents: Use the Cyan or Lime Green from the logo for thin divider lines or edge painting.
Avoid: No orange/gold (clashes with logo). No cartoon leaves.
Layout Requirements:
Front: Large, centered logo. Maybe a subtle UV gloss spot varnish over the logo icon.
Back: Name, Title, Contact Info.
Texture: Matte finish cardstock with gloss elements.
sample mock up of information on card: https://brimtolcorp-my.filedock.example/:i:/g/personal/derek_holloway_vortiqueenergy_com/AbCdEfGhIjKlMnOpQrStUvWxYz0123456789AbCdEfGh?e=X1Y2Z3
Logo: https://brimtolcorp.filedock.example/:i:/s/VortiqueEnergy/ZyXwVuTsRqPoNmLkJiHgFeDcBa9876543210ZyXwVuTs?e=Q4R5S6

```html
<!DOCTYPE html>
<html lang="en">
<head>
<meta charset="utf-8">
<title>Vortique Energy Business Card</title>
<link href="https://fonts.googleapis.com/css2?family=Montserrat:wght@300;400;500;700&display=swap" rel="stylesheet">
<style>
  :root {
    --bg: #1c1c1d;
    --card: #222223;
    --card-edge: #2c2c2e;
    --gloss: #0e0e0f;
    --gloss-text: #3a3a3c;
    --white: #f4f4f4;
    --cyan: #1fb6d9;
    --cyan-light: #35c6e0;
    --lime: #9bd13a;
    --grey: #8d8d90;
  }
  * { margin: 0; padding: 0; box-sizing: border-box; }
  html, body { width: 1200px; height: 875px; overflow: hidden; }
  body {
    background: var(--bg);
    font-family: "Montserrat", Arial, sans-serif;
    position: relative;
  }
  .card {
    position: absolute;
    width: 520px;
    height: 297px;
    top: 289px;
    border-radius: 18px;
    background: linear-gradient(160deg, var(--card-edge) 0%, var(--card) 55%, #1a1a1b 100%);
    box-shadow: 0 18px 40px rgba(0,0,0,.55);
    overflow: hidden;
  }
  .card-front { left: 50px; }
  .card-back { left: 630px; }

  /* Front */
  .front-wordmark {
    position: absolute;
    left: 0; right: 0; top: 96px;
    text-align: center;
    font-weight: 300;
    font-size: 52px;
    letter-spacing: 1px;
    color: var(--gloss-text);
  }
  .front-tagline {
    position: absolute;
    left: 0; right: 0; bottom: 62px;
    text-align: center;
    color: var(--white);
    font-weight: 700;
    font-size: 14px;
    letter-spacing: .5px;
  }

  /* Back */
  .person {
    position: absolute;
    right: 30px; top: 30px;
    text-align: right;
  }
  .person-name {
    font-size: 24px;
    color: var(--cyan-light);
    line-height: 1.1;
  }
  .person-name .first { font-weight: 700; color: var(--cyan); }
  .person-name .last { font-weight: 400; }
  .person-title {
    margin-top: 4px;
    font-size: 11px;
    color: var(--white);
    font-weight: 400;
  }
  .back-wordmark {
    position: absolute;
    left: 30px; top: 104px;
    display: flex; align-items: center; gap: 12px;
    font-weight: 300;
    font-size: 30px;
    color: var(--cyan);
  }
  .back-wordmark .mark {
    width: 26px; height: 26px;
    background: var(--cyan);
  }
  .contact {
    position: absolute;
    left: 30px; top: 168px;
    list-style: none;
    font-size: 11px;
    line-height: 17px;
    color: var(--white);
  }
  .contact li { display: flex; align-items: center; gap: 8px; }
  .contact svg { width: 11px; height: 11px; flex: none; }
  .contact .indent { padding-left: 19px; }
  .regions {
    position: absolute;
    left: 30px; bottom: 38px;
    display: flex; gap: 6px;
  }
  .region {
    width: 30px; height: 20px;
    border: 2px solid var(--white);
    border-radius: 2px;
  }
  .region-us { background: linear-gradient(180deg, #3b4f9c 0 45%, #d8d8d8 45% 60%, #c2303a 60%); }
  .region-ca { background: linear-gradient(90deg, #c9262e 0 28%, #f2f2f2 28% 72%, #c9262e 72%); }
  .region-uk { background: linear-gradient(135deg, #233f8f 0 40%, #e5e5e5 40% 46%, #c62a35 46% 54%, #e5e5e5 54% 60%, #233f8f 60%); }
  .back-tagline {
    position: absolute;
    right: 30px; bottom: 40px;
    font-size: 12.5px;
    font-weight: 500;
    color: var(--cyan);
  }
</style>
</head>
<body>
  <section class="card card-front" aria-label="Card front">
    <div class="front-wordmark">Vortique Energy</div>
    <p class="front-tagline">Rent Solar. Generate Power. Save Smarter</p>
  </section>

  <section class="card card-back" aria-label="Card back">
    <div class="person">
      <div class="person-name"><span class="first">Derek</span> <span class="last">Holloway</span></div>
      <div class="person-title">Founder / Operations Strategist</div>
    </div>

    <div class="back-wordmark"><span class="mark"></span>Vortique Energy</div>

    <ul class="contact">
      <li>
        <svg viewBox="0 0 12 12" aria-hidden="true"><path fill="#9bd13a" d="M1 4c0-2 2-3 5-3s5 1 5 3v1H8.5V4h-5v1H1zM2.5 6h7l1 5h-9z"/></svg>
        555.014.2087
      </li>
      <li>
        <svg viewBox="0 0 12 12" aria-hidden="true"><circle cx="6" cy="6" r="5" fill="none" stroke="#9bd13a" stroke-width="1.4"/><path d="M1 6h10M6 1c2 2 2 8 0 10M6 1c-2 2-2 8 0 10" fill="none" stroke="#9bd13a" stroke-width="1"/></svg>
        www.vortiqueenergy.example
      </li>
      <li class="indent">4120 Marrow Creek Drive</li>
      <li class="indent">Fairhaven, FL 30001</li>
    </ul>

    <div class="regions">
      <span class="region region-us" role="img" aria-label="United States flag"></span>
      <span class="region region-ca" role="img" aria-label="Canada flag"></span>
      <span class="region region-uk" role="img" aria-label="United Kingdom flag"></span>
    </div>

    <p class="back-tagline">No debt, no liens, no maintenance, just savings</p>
  </section>
</body>
</html>
```